Lift display layouts for global brand

We need display layouts for different sizes and applications of display. All layouts must include an arrow and floor position number. I will upload some basic examples. We want these to look modern and really eye-catching but suitable for the space it is meant for.

By "layout" we mean design specifically created for the space - including arrow, floor number, widgets / background graphics etc.
Display type ONE 15" (1024 x 768 pixels)
a. Hotel theme layout (logo, floor position, arrow and simple weather widget) [Landscape]
b. Layout displaying live TV news broadcast or similar [Landscape]
Display type TWO 10.4” (800 x 600 pixels)
a. Shopping centre layout + shop advert in main space [Landscape]
b. Office tenant standard layout + business logo in main space [Portrait]
c. Spa / Leisure Centre Layout [Landscape]
Display type 38” (1920 x 540 pixels)
a. Airport/Train station layout + flight/train departure information in main space [Landscape]
b. Restaurant layout + Menu in main space [Portrait]
c. Shopping Centre layout + Centre map in main space [Landscape]
Display type 21.5” (1920 x 1080 pixels)
a. Skyscraper layout + lift buttons and building history text [Portrait]
Display type 7” (800x480)
a. Simple lift position indicator arrow and floor [Landscape]
b. Lift position indicator with arrow and showing pictogram (Alarm, Maintenance or similar) [Landscape]

```html
<!DOCTYPE html>
<html lang="en">
<head>
<meta charset="utf-8">
<title>Lift Display Layouts</title>
<link rel="stylesheet" href="https://fonts.googleapis.com/css2?family=Montserrat:ital,wght@0,400;0,500;0,600;0,700;0,800;1,400&family=Playfair+Display:wght@800&display=swap">
<style>
:root{
  --ink:#111;
  --navy:#0a5a8e;
  --blue:#1266c8;
  --blue-dark:#0a4fa8;
  --blue-light:#6fb6ef;
  --indigo:#23418f;
  --orange:#f2701f;
  --peach:#fdd9c3;
  --pink:#f7d3df;
  --rose:#d63a5c;
  --white:#fff;
}
*{margin:0;padding:0;box-sizing:border-box}
html,body{width:1200px;height:2743px;overflow:hidden;background:var(--white)}
body{position:relative;font-family:"Montserrat",Arial,sans-serif;color:var(--ink)}
.row-label{position:absolute;left:58px;font-size:44px;font-weight:500;line-height:1}
.screen{position:absolute;overflow:hidden}
.abs{position:absolute}
.arrow{position:absolute;display:block}

/* outlined floor numerals */
.floor-numeral{position:absolute;overflow:visible}
.floor-numeral text{font-family:"Montserrat",Arial,sans-serif;font-weight:800;stroke-linejoin:round}
.floor-numeral .numeral-shadow{fill:var(--tone);stroke:var(--tone)}
.floor-numeral .numeral-face{fill:var(--white);stroke:var(--tone);paint-order:stroke fill}
.tone-indigo{--tone:var(--indigo)}
.tone-blue{--tone:var(--blue)}
.tone-rose{--tone:var(--rose)}

.solid-numeral{position:absolute;font-weight:800;line-height:1}

/* 1a hotel */
.hotel{left:155px;top:38px;width:469px;height:351px;background:linear-gradient(135deg,#e6fbff 0%,#b8ecf8 50%,#7fd8f0 100%)}
.hotel .greeting{left:30px;top:52px;width:242px;text-align:center;font-size:30px;font-weight:700;line-height:1.22;color:var(--navy)}
.hotel .floor-g{left:305px;top:150px;font-size:140px;color:var(--white);text-shadow:6px 6px 0 #0e7fb8}
.hotel .floor-name{left:306px;top:298px;font-size:28px;font-weight:600;color:var(--navy)}
.hotel .promo{left:113px;top:244px;font-size:15px;font-weight:600;line-height:1.4;color:var(--navy)}
.hotel .promo-art{left:44px;top:238px;width:58px;height:76px;border-radius:30px;background:linear-gradient(#7fd0f0,#1e76b8)}

/* 1b video */
.news{left:667px;top:38px;width:470px;height:351px;background:linear-gradient(135deg,#ddd9f9,#f3f2fd 60%,#e4e0fa)}
.news .video-caption{left:93px;top:262px;width:285px;text-align:center;font-style:italic;font-size:19px;color:var(--indigo)}

/* 2a shopping */
.mall{left:155px;top:486px;width:395px;height:296px;background:linear-gradient(160deg,#fff1e8,var(--peach) 60%,#f8b58d)}
.mall .title{left:0;top:18px;width:100%;text-align:center;font-size:25px;font-weight:700;color:var(--orange)}
.mall .slot-label{left:140px;top:142px;width:110px;text-align:center;font-style:italic;font-size:22px;line-height:1.25;color:var(--white)}

/* 2b office */
.office{left:583px;top:436px;width:298px;height:396px;background:linear-gradient(150deg,#e4f5fd,#bfe6f8 60%,#a8dcf5)}
.office .icon-caption{font-size:7px;font-weight:600;color:var(--blue)}
.office .weather{left:214px;top:12px;width:64px;height:58px}
.directory{left:60px;top:97px;width:196px;height:128px;display:grid;grid-template-columns:64px 1fr;background:rgba(255,255,255,.35)}
.directory .floors{background:rgba(120,190,235,.45);text-align:right;padding-right:7px}
.directory .names{padding-left:10px;font-weight:600;color:var(--blue-dark)}
.directory p{height:22px;line-height:22px;font-size:12.5px;white-space:nowrap}
.directory .floors p{color:var(--blue-dark);font-weight:500}
.directory .list{padding-top:8px}

/* 3 spa */
.spa{left:155px;top:896px;width:470px;height:351px;background:linear-gradient(135deg,#fbe5ec,var(--pink) 60%,#f1b3c8)}
.spa .welcome{left:240px;top:42px;width:220px;text-align:center;font-family:"Playfair Display",Georgia,serif;font-size:29px;font-weight:800;line-height:1.25;color:var(--rose);white-space:nowrap}
.spa .art{left:300px;top:126px;width:108px;height:114px;border-radius:50%;background:linear-gradient(135deg,#f6a6b9,#e35a7c)}
.spa .offer{left:258px;top:256px;width:184px;text-align:center;font-size:14.5px;font-weight:500;line-height:1.22;color:var(--rose)}
.spa .price{background:var(--rose);color:var(--white);font-weight:700;padding:0 2px}

/* 38 transport */
.transport{left:153px;top:1310px;width:985px;height:275px;background:linear-gradient(135deg,#c9ebfb,#e4f5fd 45%,#b8e3f8)}
.transport .heading{top:40px;font-size:28px;font-weight:700;color:var(--blue);line-height:38px}
.transport .badge{position:absolute;width:58px;height:58px;border:3px solid var(--blue);border-radius:50%;display:grid;place-items:center}
.timetable{position:absolute;top:105px;display:grid;grid-template-columns:138px 97px 97px;column-gap:6px;row-gap:7px}
.timetable span{height:27px;line-height:27px;text-align:center;font-size:19px;color:var(--white);border-radius:3px}
.timetable .dark{background:var(--blue)}
.timetable .light{background:var(--blue-light)}

/* 21.5 skyscraper */
.tower{left:155px;top:1657px;width:753px;height:418px;background:linear-gradient(135deg,#c4e9fa,#e6f6fd 50%,#b9e3f8)}
.tower .skyline{left:363px;top:73px;width:383px;height:298px;background:linear-gradient(180deg,rgba(18,102,200,.85),rgba(18,102,200,.15))}

/* 7 indicators */
.indicator{left:153px;width:366px;height:218px;background:linear-gradient(120deg,#f4f5f7,#e3e6ea 55%,#c9ced5)}
.indicator .floor-g{left:60px;top:50px;font-size:130px;color:var(--blue)}
.indicator-plain{top:2163px}
.indicator-service{top:2429px}
</style>
</head>
<body>

<div class="row-label" style="top:193px">1</div>
<div class="row-label" style="top:612px">2</div>
<div class="row-label" style="top:1049px">3</div>
<div class="row-label" style="top:1863px">4</div>
<div class="row-label" style="top:2249px">5</div>

<!-- 1a hotel -->
<section class="screen hotel">
  <svg class="abs" style="left:0;top:0" width="469" height="351" viewBox="0 0 469 351">
    <path d="M305 0 C270 40 300 100 280 150 C260 200 190 220 205 280 C215 320 200 340 195 351 L469 351 L469 0 Z" fill="#2cc6ec"/>
    <path d="M360 0 C330 60 360 120 340 180 C320 240 270 290 280 351 L469 351 L469 0 Z" fill="#19aedf" opacity=".6"/>
  </svg>
  <p class="abs greeting">Thank you<br>for visiting<br>today!</p>
  <svg class="arrow" style="left:315px;top:49px" width="110" height="76" viewBox="0 0 100 70" preserveAspectRatio="none">
    <polygon points="0,70 50,0 50,56" fill="#2ba0cf"/><polygon points="50,0 100,70 50,56" fill="#0d6f9e"/>
  </svg>
  <div class="abs promo-art" role="img" aria-label="Diamond ring illustration"></div>
  <p class="abs promo">Opal Lane Jewellery is<br>now open!<br>Floor 2, Area B.</p>
  <span class="solid-numeral floor-g">G</span>
  <span class="abs floor-name">Car Park</span>
</section>

<!-- 1b video -->
<section class="screen news">
  <svg class="arrow" style="left:47px;top:33px" width="110" height="73" viewBox="0 0 100 70" preserveAspectRatio="none">
    <polygon points="0,70 50,0 50,56" fill="#3a5cc8"/><polygon points="50,0 100,70 50,56" fill="#23418f"/>
  </svg>
  <svg class="floor-numeral tone-indigo" style="left:358px;top:20px" width="100" height="110" viewBox="0 0 100 110">
    <text class="numeral-shadow" x="12" y="94" font-size="100" stroke-width="10">4</text>
    <text class="numeral-face" x="6" y="88" font-size="100" stroke-width="10">4</text>
  </svg>
  <svg class="abs" width="470" height="351" viewBox="0 0 470 351">
    <polygon points="86,150 383,150 470,255 470,351 120,351 86,322" fill="#23418f"/>
    <defs><linearGradient id="vid" x1="0" y1="0" x2="1" y2="1"><stop offset="0" stop-color="#e9e6fd"/><stop offset="1" stop-color="#c7c1f5"/></linearGradient></defs>
    <rect x="93" y="156" width="285" height="160" fill="url(#vid)"/>
    <circle cx="235" cy="223" r="28" fill="#23418f"/>
    <polygon points="226,209 226,237 248,223" fill="#fff"/>
  </svg>
  <p class="abs video-caption">Video here</p>
</section>

<!-- 2a shopping -->
<section class="screen mall">
  <p class="abs title">Shopping Centre</p>
  <svg class="abs" style="left:0;top:0" width="395" height="296" viewBox="0 0 395 296">
    <path d="M120 110 C160 70 230 60 270 85 C300 100 310 140 340 165 C360 190 330 240 280 235 C240 232 210 270 160 262 C110 255 100 220 70 200 C30 175 60 140 90 140 C105 140 105 125 120 110 Z" fill="#f99154"/>
    <g fill="none" stroke="#f2701f" stroke-width="3">
      <path d="M48 97 h30 l3 8 h-36 z M50 105 v17 h26 v-17 M58 122 v-9 h10 v9"/>
      <path d="M298 82 h6 l5 16 h16 l4 -11 h-22"/>
    </g>
    <circle cx="312" cy="104" r="2.5" fill="#f2701f"/><circle cx="322" cy="104" r="2.5" fill="#f2701f"/>
    <rect x="352" y="150" width="26" height="22" rx="2" fill="#f2701f" transform="rotate(12 365 161)"/>
    <path d="M360 152 c0 -10 12 -10 12 0" fill="none" stroke="#f2701f" stroke-width="2.5" transform="rotate(12 365 161)"/>
  </svg>
  <p class="abs slot-label">Layout here</p>
</section>

<!-- 2b office -->
<section class="screen office">
  <svg class="abs" style="left:28px;top:20px" width="44" height="40" viewBox="0 0 44 40" fill="#1266c8">
    <rect x="14" y="0" width="26" height="16" rx="2"/><rect x="2" y="20" width="40" height="3"/>
    <rect x="4" y="23" width="10" height="16"/><rect x="36" y="23" width="3" height="16"/>
    <rect x="0" y="4" width="3" height="16"/>
  </svg>
  <span class="abs icon-caption" style="left:28px;top:63px">Workspace</span>
  <svg class="abs weather" viewBox="0 0 64 58">
    <circle cx="32" cy="30" r="28" fill="#1266c8"/>
    <circle cx="42" cy="22" r="6" fill="#f5a623"/>
    <path d="M16 38 a8 8 0 0 1 4 -15 a10 10 0 0 1 19 -2 a8 8 0 0 1 8 17 z" fill="#fff"/>
    <rect x="6" y="46" width="52" height="11" rx="5.5" fill="#fff" stroke="#1266c8" stroke-width="1.5"/>
    <text x="32" y="54" text-anchor="middle" font-family="Montserrat,Arial,sans-serif" font-size="6.5" font-weight="600" fill="#1266c8">Description</text>
  </svg>
  <div class="abs directory">
    <div class="floors list"><p>Ground</p><p>One</p><p>Two</p><p>Three</p><p>Four</p></div>
    <div class="names list"><p>Reception</p><p>Norbridge &amp; Co</p><p>Quillworks</p><p>Tarn Group</p><p>Brightform</p></div>
  </div>
  <svg class="floor-numeral tone-blue" style="left:42px;top:250px" width="110" height="130" viewBox="0 0 110 130">
    <text class="numeral-shadow" x="10" y="108" font-size="110" stroke-width="9">3</text>
    <text class="numeral-face" x="5" y="103" font-size="110" stroke-width="9">3</text>
  </svg>
  <svg class="arrow" style="left:180px;top:293px" width="92" height="64" viewBox="0 0 100 70" preserveAspectRatio="none">
    <polygon points="0,0 50,14 50,70" fill="#4aa3e0"/><polygon points="50,14 100,0 50,70" fill="#1266c8"/>
  </svg>
</section>

<!-- 3 spa -->
<section class="screen spa">
  <svg class="arrow" style="left:47px;top:41px" width="140" height="98" viewBox="0 0 100 70" preserveAspectRatio="none">
    <polygon points="0,70 50,0 50,56" fill="#f48aa0"/><polygon points="50,0 100,70 50,56" fill="#e0475e"/>
  </svg>
  <svg class="floor-numeral tone-rose" style="left:52px;top:180px" width="140" height="170" viewBox="0 0 140 170">
    <text class="numeral-shadow" x="11" y="143" font-size="145" stroke-width="10">3</text>
    <text class="numeral-face" x="6" y="138" font-size="145" stroke-width="10">3</text>
  </svg>
  <p class="abs welcome">Welcome to<br>Willow Spa!</p>
  <div class="abs art" role="img" aria-label="Spa wellbeing illustration with flowers and leaves"></div>
  <p class="abs offer">Book now for a free pedicure with every treatment over <span class="price">£50</span></p>
</section>

<!-- 38 transport -->
<section class="screen transport">
  <div class="badge" style="left:136px;top:30px">
    <svg width="32" height="32" viewBox="0 0 32 32" fill="#1266c8"><path d="M15 2 h2 l1 11 l12 6 v3 l-12 -3 l-1 7 l4 3 v2 l-5 -1.5 l-5 1.5 v-2 l4 -3 l-1 -7 l-12 3 v-3 l12 -6 z"/></svg>
  </div>
  <p class="abs heading" style="left:214px">Airport</p>
  <div class="timetable" style="left:61px">
    <span class="dark">Dep</span><span class="dark">Time</span><span class="dark">Time</span>
    <span class="light">Dep</span><span class="light">Time</span><span class="light">Time</span>
    <span class="dark">Dep</span><span class="dark">Time</span><span class="dark">Time</span>
    <span class="light">Dep</span><span class="light">Time</span><span class="light">Time</span>
  </div>
  <svg class="arrow" style="left:446px;top:21px" width="92" height="63" viewBox="0 0 100 70" preserveAspectRatio="none">
    <polygon points="0,70 50,0 50,56" fill="#1266c8"/><polygon points="50,0 100,70 50,56" fill="#4aa3e0"/>
  </svg>
  <svg class="arrow" style="left:446px;top:188px" width="92" height="64" viewBox="0 0 100 70" preserveAspectRatio="none">
    <polygon points="0,0 50,14 50,70" fill="#4aa3e0"/><polygon points="50,14 100,0 50,70" fill="#1266c8"/>
  </svg>
  <p class="abs heading" style="right:176px">Train Station</p>
  <div class="badge" style="left:827px;top:30px">
    <svg width="30" height="32" viewBox="0 0 30 32" fill="none" stroke="#1266c8" stroke-width="2.5"><rect x="5" y="2" width="20" height="20" rx="5"/><path d="M5 12 h20 M10 28 l-4 3 M20 28 l4 3 M9 22 l-2 6 h16 l-2 -6"/></svg>
  </div>
  <div class="timetable" style="left:578px">
    <span class="dark">Dep</span><span class="dark">Time</span><span class="dark">Time</span>
    <span class="light">Dep</span><span class="light">Time</span><span class="light">Time</span>
    <span class="dark">Dep</span><span class="dark">Time</span><span class="dark">Time</span>
    <span class="light">Dep</span><span class="light">Time</span><span class="light">Time</span>
  </div>
</section>

<!-- 21.5 skyscraper -->
<section class="screen tower">
  <svg class="arrow" style="left:115px;top:37px" width="164" height="112" viewBox="0 0 100 70" preserveAspectRatio="none">
    <polygon points="0,70 50,0 50,56" fill="#1266c8"/><polygon points="50,0 100,70 50,56" fill="#4aa3e0"/>
  </svg>
  <svg class="floor-numeral tone-blue" style="left:108px;top:190px" width="190" height="215" viewBox="0 0 190 215">
    <text class="numeral-shadow" x="16" y="180" font-size="185" stroke-width="12">4</text>
    <text class="numeral-face" x="8" y="172" font-size="185" stroke-width="12">4</text>
  </svg>
  <div class="abs skyline" role="img" aria-label="City skyscraper skyline illustration"></div>
</section>

<!-- 7 plain indicator -->
<section class="screen indicator indicator-plain">
  <span class="solid-numeral floor-g">G</span>
  <svg class="arrow" style="left:269px;top:38px" width="72" height="47" viewBox="0 0 100 70" preserveAspectRatio="none">
    <polygon points="0,70 50,0 50,56" fill="#1266c8"/><polygon points="50,0 100,70 50,56" fill="#4aa3e0"/>
  </svg>
  <span class="abs" style="left:287px;top:111px;width:36px;height:2px;background:#4aa3e0"></span>
  <svg class="arrow" style="left:269px;top:140px" width="72" height="47" viewBox="0 0 100 70" preserveAspectRatio="none">
    <polygon points="0,0 50,14 50,70" fill="#4aa3e0"/><polygon points="50,14 100,0 50,70" fill="#1266c8"/>
  </svg>
</section>

<!-- 7 maintenance indicator -->
<section class="screen indicator indicator-service">
  <span class="solid-numeral floor-g">G</span>
  <svg class="arrow" style="left:269px;top:21px" width="72" height="47" viewBox="0 0 100 70" preserveAspectRatio="none">
    <polygon points="0,70 50,0 50,56" fill="#1266c8"/><polygon points="50,0 100,70 50,56" fill="#4aa3e0"/>
  </svg>
  <svg class="abs" style="left:279px;top:81px" width="52" height="52" viewBox="0 0 52 52" fill="none" stroke="#1266c8" stroke-width="5" stroke-linecap="round">
    <path d="M10 42 l24 -24"/><circle cx="38" cy="14" r="7"/>
    <path d="M14 10 l28 28"/><path d="M8 8 l6 2 l2 6"/>
  </svg>
  <svg class="arrow" style="left:269px;top:159px" width="72" height="47" viewBox="0 0 100 70" preserveAspectRatio="none">
    <polygon points="0,0 50,14 50,70" fill="#4aa3e0"/><polygon points="50,14 100,0 50,70" fill="#1266c8"/>
  </svg>
</section>

</body>
</html>
```